Home based bath & shave business wants to redesign labels

I would like to have new labels designed to fit the body lotion and bath oil bottles. We want them similar but different. The key ingredient for all of Ferrucci's Bath & Shave products is olive oil.

You are free to change colors. I have attached our logo and current labels. The current labels just don't look right to me (pictures attached). I like the script font, but am willing to entertain another. I have our logo in several formats and the font, should you want it.

Target Market(s)

Women

Industry/Entity Type

Business

Font styles to use
Decorative
Script

Requirements
Must have
• Both product labels must include our logo.The logo must stay the same though to make it work with the label, you can change the color if needed.
• It should be a vertical label.
• The bottle used is a 8 oz Clear PET Tapered Naples Oval Bottle (I have attached pictures) and its dimensions are:
• Length 2.548 in / 6.472 cm
• Width 1.479 in / 3.757 cm
• Height 6.639 in / 16.863 cm

```html
<!DOCTYPE html>
<html lang="en">
<head>
<meta charset="utf-8">
<title>Ferrucci's Bath &amp; Shave — Label Designs</title>
<link rel="stylesheet" href="https://fonts.googleapis.com/css2?family=Michroma&family=Arimo:wght@400&display=swap">
<style>
  :root {
    --ink: #0b0b0c;
    --white: #ffffff;
    --plum: #8e1f86;
    --plum-light: #d98be0;
    --mint: #3ef27a;
    --mint-light: #59e7a8;
    --grey-light: #f4f4f4;
    --grey-mid: #a8a8a8;
    --grey-dark: #5c5c5c;
    --caption: #d6d6d6;
  }
  * { margin: 0; padding: 0; box-sizing: border-box; }
  html, body { width: 1200px; height: 960px; overflow: hidden; background: var(--ink); }
  .board { position: relative; width: 1200px; height: 960px; background: var(--ink); overflow: hidden; }

  .panel { position: absolute; }

  .label-lotion {
    left: 0; top: 0; width: 672px; height: 432px;
    background: linear-gradient(to bottom, var(--plum) 0, var(--ink) 85px, var(--ink) 372px, var(--plum) 432px);
  }
  .label-oil {
    left: 528px; top: 455px; width: 672px; height: 435px;
    background: linear-gradient(to bottom, var(--mint) 0, var(--ink) 90px, var(--ink) 375px, var(--mint) 435px);
  }
  .stage-lotion {
    left: 672px; top: 0; width: 528px; height: 455px;
    background: linear-gradient(to bottom, var(--grey-mid) 0, var(--grey-light) 45%, var(--white) 60%, var(--grey-mid) 100%);
  }
  .stage-oil {
    left: 0; top: 503px; width: 528px; height: 457px;
    background: linear-gradient(to bottom, var(--grey-dark) 0, #1a1a1a 100%);
  }

  .brand-name {
    position: absolute; left: 0; right: 0;
    text-align: center;
    font-family: "Michroma", sans-serif;
    font-weight: 400;
    font-size: 30px;
    line-height: 1.5;
    letter-spacing: 1px;
  }
  .label-lotion .brand-name { top: 160px; color: var(--plum-light); }
  .label-oil .brand-name { top: 160px; color: var(--mint-light); }

  .product-name {
    position: absolute; left: 0; right: 0;
    text-align: center;
    font-family: "Michroma", sans-serif;
    font-size: 66px;
    color: var(--white);
    letter-spacing: 2px;
    line-height: 1;
  }
  .label-lotion .product-name { top: 292px; }
  .label-oil .product-name { top: 296px; padding-right: 20px; }

  .ingredients {
    position: absolute;
    font-family: "Arimo", sans-serif;
    color: var(--caption);
    display: flex;
  }
  .ingredients-lotion { left: 7px; top: 441px; font-size: 9.5px; line-height: 12px; }
  .ingredients-lotion .ingredients-title { width: 62px; }
  .ingredients-oil { left: 796px; top: 938px; font-size: 18px; line-height: 22px; align-items: baseline; }
  .ingredients-oil .ingredients-list { font-size: 14px; margin-left: 10px; }

  .bottle-shot { position: absolute; }
  .stage-lotion .bottle-shot { left: 210px; top: 30px; }
  .stage-oil .bottle-shot { left: 196px; top: 42px; }
</style>
</head>
<body>
<main class="board">

  <section class="panel label-lotion">
    <p class="brand-name">Ferrucci's<br>Bath &amp; Shave</p>
    <h1 class="product-name">BODY LOTION</h1>
  </section>

  <div class="ingredients ingredients-lotion">
    <span class="ingredients-title">Ingridients</span>
    <span class="ingredients-list">Water, Olive Oil, Aloe Vera Juice, Avocado Oil<br>Rice Bran Oil, BTMS-50, Glycerin, Stearyl Alcohol<br>Oat Extract, DL Panthenol, Optiphen Buckthorn Extract<br>Vitamin E, and Fragrance Oil</span>
  </div>

  <section class="panel stage-lotion">
    <svg class="bottle-shot" width="130" height="410" viewBox="0 0 130 410" role="img" aria-label="Photo of the clear tapered bottle wearing the body lotion label">
      <defs>
        <linearGradient id="lotionShot" x1="0" y1="0" x2="1" y2="0">
          <stop offset="0" stop-color="#d9d9d9"/>
          <stop offset="0.5" stop-color="#f7f7f7"/>
          <stop offset="1" stop-color="#cfcfcf"/>
        </linearGradient>
      </defs>
      <rect width="130" height="410" fill="url(#lotionShot)"/>
    </svg>
  </section>

  <section class="panel stage-oil">
    <svg class="bottle-shot" width="136" height="405" viewBox="0 0 136 405" role="img" aria-label="Photo of the clear tapered bottle wearing the bath oil label">
      <defs>
        <linearGradient id="oilShot" x1="0" y1="0" x2="1" y2="0">
          <stop offset="0" stop-color="#4a4a4a"/>
          <stop offset="0.5" stop-color="#8a8a8a"/>
          <stop offset="1" stop-color="#3e3e3e"/>
        </linearGradient>
      </defs>
      <rect width="136" height="405" fill="url(#oilShot)"/>
    </svg>
  </section>

  <section class="panel label-oil">
    <p class="brand-name">Ferrucci's<br>Bath &amp; Shave</p>
    <h1 class="product-name">BATH OIL</h1>
  </section>

  <div class="ingredients ingredients-oil">
    <span class="ingredients-title">Ingridients</span>
    <span class="ingredients-list">Olive Oil, Grape seed Oil, and Fragrance Oil</span>
  </div>

</main>
</body>
</html>
```